Gains Beyond the Lantern Gate - book cover design

I need a cover designed for a new book (paperback and eBook).
The title is: “Gains Beyond the Lantern Gate” with the subtitle: “The only book you need to start investing profitably in Chinese stocks”. It is from the first time author :“Teemu Harkala“.
The following text should also be visible in the front cover: “From the founder of OrientWagerly.com” or "Founder of OrientWagerly.com".
The publisher’s logo, should also be visible somewhere on the cover (front, back or spine). The logo, along with source files are here: http://filevault.example/k7Tq2Lp
The book/paperback cover dimensions are: 5.06 x 7.81 inches (12.9 x 19.8 centimeters). Here are the book-cover templates recommended by Bookdale for a book of this size:
http://filevault.example/z3Wm9Xa (.indd)
http://filevault.example/r8Nd4Fu (.pdf)
Below is a description of the book. I don't have a specific idea or vision in mind for the cover. I'd like to see what designs and ideas ArtHuddle designers come up with.
Color red is usually associated with China, but I don’t want the book to be red. Instead the background color could be one of the publisher’s brand colors (#88C198, #017487). However I’ll leave you the designers freedom to propose any colors and combinations.
This is not an entry level book, but a very advanced level investment strategy book for international investors. It explains with concrete examples how non-Chinese citizens can best benefit from China’s economic miracle by picking the best Chinese growth stocks from New York, Hong Kong and Singapore stock exchanges.
The book cover should not have dollar signs promising easy and fast money (because easy and fast money doesn’t exist). What the book promises is a very advanced level China investing strategy, which will considerably improve international investors’ odds for big profits in the longer term.
The big investment themes in the book are China’s consumer sector and service industries.
The book cover should have some kind of reference/association to Investing and China.
The design needs to work and be effective at both a large book cover size and a small thumbnail-sized image - the way that many people browse book covers on Bookdale and other websites. Therefore, a design that relies on really small details probably won't translate at the smaller image sizes that book covers are displayed online.
Target Market(s)
International investors (~50% from western countries, 30% from Singapore/Hong Kong, Malaysia)
Industry/Entity Type
Investment
Font styles to use
Other font styles liked:
- EB Garamond, Grimson text or some other beautiful book font
Look and feel
Each slider illustrates characteristics of the customer's brand and the style your logo design should communicate.

```html
<!DOCTYPE html>
<html lang="en">
<head>
<meta charset="utf-8">
<title>Gains Beyond the Lantern Gate – Teemu Harkala</title>
<link href="https://fonts.googleapis.com/css2?family=Jost:ital,wght@0,300;0,400;1,300&family=Oswald:wght@500&family=Yellowtail&display=swap" rel="stylesheet">
<style>
  :root {
    --paper: #ffffff;
    --gate-tint-strong: rgba(175, 79, 80, 0.20);
    --gate-tint-soft: rgba(175, 79, 80, 0.08);
    --title: #be1e2d;
    --ink-soft: #555559;
    --author: #4a393c;
    --publisher: #ba1f2b;
  }
  html, body {
    margin: 0;
    padding: 0;
    width: 768px;
    height: 1200px;
    overflow: hidden;
    background: var(--paper);
  }
  .cover {
    position: relative;
    width: 768px;
    height: 1200px;
    overflow: hidden;
    background: var(--paper);
  }
  .gate-artwork {
    position: absolute;
    left: 46px;
    top: 157px;
    width: 673px;
    height: 843px;
    background: linear-gradient(180deg, var(--gate-tint-strong), var(--gate-tint-soft));
  }
  .tagline {
    position: absolute;
    top: 64px;
    left: 0;
    width: 100%;
    margin: 0;
    text-align: center;
    font-family: "Jost", sans-serif;
    font-style: italic;
    font-weight: 300;
    font-size: 28px;
    letter-spacing: 2.6px;
    color: var(--ink-soft);
  }
  .title {
    position: absolute;
    top: 380px;
    left: 154px;
    margin: 0;
    font-family: "Jost", sans-serif;
    font-weight: 300;
    font-size: 80px;
    line-height: 80px;
    color: var(--title);
    text-transform: uppercase;
    letter-spacing: 1px;
  }
  .title-line { display: block; white-space: nowrap; }
  .title-article {
    font-family: "Yellowtail", cursive;
    text-transform: none;
    font-size: 40px;
    letter-spacing: 0;
    margin-right: 6px;
    vertical-align: 6px;
  }
  .subtitle {
    position: absolute;
    top: 790px;
    left: 0;
    width: 100%;
    margin: 0;
    text-align: center;
    font-family: "Jost", sans-serif;
    font-weight: 300;
    font-size: 29px;
    line-height: 35px;
    letter-spacing: 2.4px;
    color: var(--ink-soft);
  }
  .publisher-mark {
    position: absolute;
    left: -4px;
    top: 1056px;
    width: 154px;
    height: 154px;
    border-radius: 50%;
    background: var(--publisher);
  }
  .author {
    position: absolute;
    top: 1084px;
    left: 213px;
    width: 488px;
    margin: 0;
    text-align: center;
    font-family: "Oswald", sans-serif;
    font-weight: 500;
    font-size: 58px;
    line-height: 70px;
    letter-spacing: 8px;
    color: var(--author);
    text-transform: uppercase;
    white-space: nowrap;
  }
</style>
</head>
<body>
  <main class="cover">
    <div class="gate-artwork" role="img" aria-label="Red torii gate illustration framing the title"></div>

    <p class="tagline">From the founder of OrientWagerly.com</p>

    <h1 class="title">
      <span class="title-line">Gains</span>
      <span class="title-line">Beyond</span>
      <span class="title-line"><span class="title-article">the</span>Lantern</span>
      <span class="title-line">Gate</span>
    </h1>

    <p class="subtitle">The only book you need to<br>start investing profitably in<br>Chinese stocks</p>

    <div class="publisher-mark" aria-hidden="true"></div>

    <p class="author">Teemu Harkala</p>
  </main>
</body>
</html>
```